Outpost Lattice Advisors – Franchise Growth & Development Presentation

Outpost Lattice Advisors is an outsourced franchise sales organization (FSO) that helps franchisors grow their franchise systems without the expense and risk of hiring an internal franchise development team.

We are seeking a professional PowerPoint presentation that will be used to present our services to franchisors, franchise executives, founders, and growth-stage franchise brands.

The presentation should communicate the value of partnering with Outpost Lattice Advisors, including:

• Fractional franchise sales team versus hiring internal staff
• 30+ years of franchise industry experience
• 550+ franchise sales successes
• Immediate access to established franchise broker relationships
• Proven franchise development processes
• Franchise growth strategy and enterprise value creation
• Potential private equity and exit opportunities through franchise expansion

The presentation should feel like a modern consulting, investment, or growth strategy presentation rather than a typical sales brochure. We want strong visual storytelling, custom infographics, professional diagrams, and clean business-oriented design.

The audience includes business owners, franchise founders, franchise executives, and investors who are evaluating growth strategies for their franchise systems.

Target Market(s)

Primary Audience: Emerging franchisors Growth-stage franchise brands Franchise founders Franchise CEOs Franchise presidents Franchise development executives Secondary Audience: Private equity firms Franchise investors Strategic buyers Franchise consultants

Industry/Entity Type

Franchise Development, Private Equity / Business Expansion

Font styles to use
Other font styles liked:
• Use Montserrat for titles and Open Sans for body text.

Requirements
Must have
• Modern professional business design Consistent branding throughout Custom infographics Comparison graphics Broker network ecosystem graphic Enterprise value graphic Easy-to-read charts and visuals Editable PowerPoint format Professional iconography. www.outpostlatticeadvisors.example as reference for colors
Nice to have
• Franchise-related imagery Subtle growth-themed visuals Timeline graphics Data visualization Private equity / valuation style graphics
Should not have
• Cartoon graphics Clip art Overly busy slides Stock-template appearance Bright neon colors Handwritten fonts Excessive text on slides Juvenile or playful design elements

```html
<!DOCTYPE html>
<html lang="en">
<head>
<meta charset="utf-8">
<title>Outpost Lattice Advisors – Presentation Overview</title>
<link rel="stylesheet" href="https://fonts.googleapis.com/css2?family=Montserrat:ital,wght@0,400;0,600;0,700;0,800;1,700&family=Open+Sans:wght@400;600;700&display=swap">
<style>
  :root {
    --navy: #13294b;
    --navy-deep: #0d1f3b;
    --navy-soft: #2c4468;
    --orange: #f7971d;
    --white: #ffffff;
    --canvas: #e3e3e3;
    --ink: #1d2a3d;
    --head: "Montserrat", sans-serif;
    --body: "Open Sans", sans-serif;
  }
  * { margin: 0; padding: 0; box-sizing: border-box; }
  html, body { width: 1200px; height: 1200px; overflow: hidden; background: var(--canvas); }
  .board { position: relative; width: 1200px; height: 1200px; }
  .slide { position: absolute; width: 481px; height: 271px; overflow: hidden; background: var(--white); }
  .slide svg { display: block; width: 481px; height: 271px; }
  .abs { position: absolute; }

  .brand-mark { font-family: var(--head); font-weight: 700; color: var(--white); letter-spacing: .02em; white-space: nowrap; }
  .brand-badge { position: absolute; background: var(--navy); border-radius: 3px; display: flex; align-items: center; justify-content: center; font-family: var(--head); font-weight: 700; color: var(--white); white-space: nowrap; }

  /* Slide 1 – cover */
  .cover .hero { left: 0; top: 0; width: 481px; height: 213px; background: linear-gradient(120deg, #1c3358 0%, #2b4468 55%, #1a2f52 100%); }
  .cover .title { left: 48px; top: 70px; font-family: var(--head); font-weight: 700; font-size: 21px; line-height: 27px; color: var(--white); }
  .cover .title .accent { color: var(--orange); }
  .cover .promise { left: 207px; top: 176px; width: 236px; height: 60px; background: var(--orange); border-radius: 6px; padding: 10px 14px 0 23px; font-family: var(--head); font-size: 8.6px; line-height: 12.5px; color: var(--white); }
  .cover .promise b { color: var(--navy); font-weight: 700; }
  .cover .rule { left: 44px; top: 250px; width: 283px; height: 1.5px; background: var(--orange); }
  .cover .url { left: 337px; top: 245px; font-family: var(--head); font-size: 6.2px; color: var(--navy); }

  /* Slide 2 – challenge */
  .challenge .band { left: 0; top: 59px; width: 481px; height: 212px; background: var(--navy); }
  .challenge .photo { left: 230px; top: 59px; width: 251px; height: 212px; background: linear-gradient(90deg, rgba(19,41,75,1) 0%, #55698a 45%, #8d9bb1 75%, #b8c0cc 100%); }
  .challenge .tab { left: 37px; top: 27px; width: 242px; height: 64px; background: var(--orange); border-radius: 6px; padding: 14px 0 0 21px; font-family: var(--head); font-weight: 700; font-size: 15.5px; line-height: 17px; color: var(--navy); }
  .challenge .points { left: 57px; top: 108px; list-style: none; font-family: var(--body); font-size: 10px; line-height: 12px; color: var(--white); }
  .challenge .points li { position: relative; padding-left: 9px; margin-bottom: 6px; }
  .challenge .points li::before { content: "•"; position: absolute; left: 0; top: 0; }
  .challenge .points li.dot-accent::before { color: var(--orange); }
  .challenge .points em { font-style: normal; color: var(--orange); }
  .challenge .rule { left: 37px; top: 243px; width: 242px; height: 1.5px; background: var(--orange); }

  /* Slide 3 – why us */
  .why .panel { left: 192px; top: 0; width: 289px; height: 271px; background: linear-gradient(135deg, #243c61 0%, #1a3054 60%, #13294b 100%); }
  .why .bar { left: 0; top: 107px; width: 10px; height: 130px; background: var(--orange); }
  .why .heading { left: 33px; top: 106px; font-family: var(--head); font-weight: 800; font-size: 19px; line-height: 22px; color: var(--ink); }
  .why .heading span { color: var(--orange); }
  .why .stat { width: 122px; white-space: nowrap; font-family: var(--body); font-size: 10.8px; line-height: 13px; color: var(--white); }
  .why .stat b { font-weight: 700; }
  .why .stat em { font-style: normal; font-weight: 700; color: var(--orange); }
  .why .stat .num { font-family: var(--head); font-weight: 700; font-size: 19px; line-height: 22px; color: var(--orange); }
  .why .stat .num small { font-size: 12px; font-weight: 600; }
  .why .line { width: 85px; height: 1.5px; background: var(--orange); }

  .svg-head { font-family: var(--head); }
  .svg-body { font-family: var(--body); }
</style>
</head>
<body>
<main class="board">

  <!-- Slide 1: Cover -->
  <section class="slide cover" style="left:98px; top:142px;">
    <div class="abs hero" role="img" aria-label="Business team meeting around a whiteboard, in dark blue tones"></div>
    <div class="abs brand-mark" style="left:45px; top:20px; font-size:9.5px;">OUTPOST LATTICE ADVISORS</div>
    <div class="abs" style="left:45px; top:35px; width:134px; height:1px; background:var(--orange);"></div>
    <h1 class="abs title">Outsourced<br>Franchise Sales<br><span class="accent">&amp; Growth<br>Experts</span></h1>
    <p class="abs promise">Helping <b>franchisors grow faster</b> without the cost and risk of building an internal franchise development team.</p>
    <div class="abs rule"></div>
    <div class="abs url">www.outpostlatticeadvisors.example</div>
  </section>

  <!-- Slide 2: Challenge -->
  <section class="slide challenge" style="left:620px; top:142px;">
    <div class="abs band"></div>
    <div class="abs photo" role="img" aria-label="Two colleagues reviewing work on a laptop in an office"></div>
    <h2 class="abs tab">The Challenge Facing<br>Emerging Franchisors</h2>
    <ul class="abs points">
      <li>Limited franchise <em>sales resources</em></li>
      <li class="dot-accent"><em>Founder</em> wearing too many hats</li>
      <li>Inconsistent lead <em>follow-up</em></li>
      <li>Difficulty <em>recruiting</em> franchisees</li>
      <li>Lack of <em>broker</em> relationships</li>
      <li>High cost of internal franchise<br><em>development staff</em></li>
    </ul>
    <div class="abs rule"></div>
    <div class="brand-badge" style="left:397px; top:253px; width:76px; height:14px; font-size:4.6px;">OUTPOST LATTICE ADVISORS</div>
  </section>

  <!-- Slide 3: Why us -->
  <section class="slide why" style="left:98px; top:448px;">
    <div class="abs panel" role="img" aria-label="Senior executive in a meeting, in dark blue tones"></div>
    <div class="abs bar"></div>
    <h2 class="abs heading">WHY<br><span>Outpost<br>Lattice<br>Advisors</span></h2>
    <div class="brand-badge" style="left:30px; top:212px; width:134px; height:25px; font-size:7.6px;">OUTPOST LATTICE ADVISORS</div>

    <div class="abs stat" style="left:228px; top:43px;"><div class="num">30+ <small>years</small></div>franchise industry<br><b>experience</b></div>
    <div class="abs stat" style="left:352px; top:43px;"><div class="num">500+</div>franchise <em>sales</em><br>successes</div>
    <div class="abs line" style="left:225px; top:100px;"></div>
    <div class="abs line" style="left:349px; top:100px;"></div>

    <div class="abs stat" style="left:228px; top:119px;">Fractional<br>franchise<br><b>sales team</b></div>
    <div class="abs stat" style="left:352px; top:119px;">Proven<br><b>systems and<br>processes</b></div>
    <div class="abs line" style="left:225px; top:166px;"></div>
    <div class="abs line" style="left:349px; top:166px;"></div>

    <div class="abs stat" style="left:228px; top:188px;">Deep <b>broker</b><br>network<br>relationships</div>
    <div class="abs stat" style="left:352px; top:188px;">Immediate<br><b>execution</b></div>
    <div class="abs line" style="left:225px; top:236px;"></div>
    <div class="abs line" style="left:349px; top:236px;"></div>
  </section>

  <!-- Slide 4: Cost comparison -->
  <section class="slide cost" style="left:620px; top:448px;">
    <svg viewBox="0 0 775 436" aria-label="Cost of hiring versus outsourcing comparison">
      <defs>
        <linearGradient id="header-fade" x1="0" y1="0" x2="0" y2="1">
          <stop offset="0" stop-color="#13294b"/><stop offset="1" stop-color="#0d1f3b"/>
        </linearGradient>
        <linearGradient id="ring-navy" x1="0" y1="0" x2="1" y2="0">
          <stop offset="0" stop-color="#13294b"/><stop offset="1" stop-color="#c5ccd8"/>
        </linearGradient>
        <linearGradient id="ring-orange" x1="0" y1="0" x2="1" y2="0">
          <stop offset="0" stop-color="#fde2bf"/><stop offset="1" stop-color="#f7971d"/>
        </linearGradient>
      </defs>
      <rect width="775" height="89" fill="url(#header-fade)"/>
      <text x="387" y="59" text-anchor="middle" class="svg-head" font-size="26" font-weight="700" fill="#fff">The Cost of Hiring <tspan fill="#f7971d">vs. Outsourcing</tspan></text>

      <g class="svg-body" font-size="14" font-weight="700" fill="#1d2a3d" text-anchor="end">
        <text x="158" y="154">Recruiting costs</text>
        <text x="158" y="186">Salary</text>
        <text x="158" y="217">Benefits</text>
        <text x="158" y="248">Payroll taxes</text>
        <text x="158" y="280">Training</text>
        <text x="158" y="312">Ramp-up period</text>
        <text x="158" y="344">Unknown</text>
        <text x="158" y="359">performance</text>
      </g>
      <g fill="none" stroke="#13294b" stroke-width="1.2">
        <polyline points="168,150 265,150 260,180"/>
        <polyline points="168,181 230,181 246,196"/>
        <polyline points="168,213 220,213 235,218"/>
        <polyline points="168,244 229,243"/>
        <polyline points="168,276 215,276 230,268"/>
        <polyline points="168,307 222,307 238,291"/>
        <polyline points="168,348 240,348 251,312"/>
      </g>
      <path d="M269.5 173 A95 95 0 0 0 269.5 329" fill="none" stroke="url(#ring-navy)" stroke-width="14"/>
      <g fill="#fff" stroke="#13294b" stroke-width="1.5">
        <circle cx="260" cy="180" r="4"/><circle cx="246" cy="196" r="4"/><circle cx="235" cy="218" r="4"/>
        <circle cx="229" cy="243" r="4"/><circle cx="230" cy="268" r="4"/><circle cx="238" cy="291" r="4"/>
        <circle cx="251" cy="312" r="4"/>
      </g>
      <circle cx="324" cy="251" r="67" fill="#13294b"/>
      <g class="svg-body" font-size="12.5" fill="#fff" text-anchor="middle">
        <text x="318" y="234">Internal</text><text x="318" y="250">Franchise</text>
        <text x="318" y="266">Development</text><text x="318" y="282">Director</text>
      </g>

      <line x1="379" y1="109" x2="379" y2="397" stroke="#f7971d" stroke-width="2"/>
      <path d="M408 134 A108 108 0 1 1 408 337" fill="none" stroke="url(#ring-orange)" stroke-width="14"/>
      <g fill="#fff" stroke="#f7971d" stroke-width="1.5">
        <circle cx="473" cy="132" r="4"/><circle cx="521" cy="160" r="4"/><circle cx="549" cy="208" r="4"/>
        <circle cx="551" cy="255" r="4"/><circle cx="533" cy="298" r="4"/><circle cx="491" cy="334" r="4"/>
      </g>
      <circle cx="445" cy="236" r="80" fill="#f7971d"/>
      <g class="svg-head" font-size="16" font-weight="700" fill="#13294b" text-anchor="middle">
        <text x="444" y="202">Outpost</text><text x="444" y="221">Lattice</text><text x="444" y="240">Advisors</text>
      </g>
      <rect x="384" y="254" width="124" height="20" rx="3" fill="#13294b"/>
      <text x="446" y="267" text-anchor="middle" class="svg-head" font-size="7" font-weight="700" fill="#fff">OUTPOST LATTICE ADVISORS</text>

      <g fill="none" stroke="#f7971d" stroke-width="1.2">
        <polyline points="473,132 498,140 596,140"/>
        <polyline points="521,160 546,190 596,190"/>
        <polyline points="549,208 574,236 596,236"/>
        <polyline points="551,255 574,276 596,276"/>
        <polyline points="533,298 558,316 596,316"/>
        <polyline points="491,334 516,369 596,369"/>
      </g>
      <g class="svg-head" font-size="14" font-weight="700" fill="#f7971d">
        <text x="606" y="140">Fractional</text><text x="606" y="154">investment</text>
        <text x="606" y="190">Entire team</text><text x="606" y="204">of experts</text>
        <text x="606" y="241">Immediate launch</text>
        <text x="606" y="281">Prove&#160; processes</text>
        <text x="606" y="321">Existing</text><text x="606" y="335">relationships</text>
        <text x="606" y="374">Scalable growth</text>
      </g>
      <rect x="641" y="408" width="123" height="22" rx="4" fill="#13294b"/>
      <text x="702" y="422" text-anchor="middle" class="svg-head" font-size="7.2" font-weight="700" fill="#fff">OUTPOST LATTICE ADVISORS</text>
    </svg>
  </section>

  <!-- Slide 5: Day one -->
  <section class="slide day-one" style="left:98px; top:753px;">
    <svg viewBox="0 0 775 436" aria-label="What takes years to build, you get on day one">
      <defs>
        <linearGradient id="top-band" x1="0" y1="0" x2="1" y2="1">
          <stop offset="0" stop-color="#1e3559"/><stop offset="1" stop-color="#13294b"/>
        </linearGradient>
        <linearGradient id="halo" x1="0" y1="0" x2="1" y2="1">
          <stop offset="0" stop-color="#fde2bf"/><stop offset=".6" stop-color="#f7971d"/><stop offset="1" stop-color="#f7971d"/>
        </linearGradient>
        <g id="medal">
          <circle r="66" fill="url(#halo)"/>
          <circle r="59" fill="#fff"/>
          <circle r="53" fill="#13294b"/>
        </g>
      </defs>
      <rect width="775" height="224" fill="url(#top-band)" role="img" aria-label="Faint gears and risk management words in dark blue"/>
      <line x1="78" y1="55" x2="214" y2="55" stroke="#fff" stroke-width="1.5"/>
      <line x1="540" y1="55" x2="675" y2="55" stroke="#fff" stroke-width="1.5"/>
      <text x="377" y="62" text-anchor="middle" class="svg-head" font-size="21" font-weight="700" fill="#fff">What Takes Years to Build,</text>
      <text x="380" y="102" text-anchor="middle" class="svg-head" font-size="36" font-weight="700" fill="#f7971d">You Get on Day One</text>

      <use href="#medal" x="160" y="224"/><use href="#medal" x="313" y="224"/>
      <use href="#medal" x="465" y="224"/><use href="#medal" x="618" y="224"/>
      <use href="#medal" x="236" y="338"/><use href="#medal" x="388" y="338"/><use href="#medal" x="541" y="338"/>

      <g class="svg-body" font-size="12.5" font-weight="700" fill="#fff" text-anchor="middle">
        <text x="160" y="214">Franchise</text><text x="160" y="228">broker</text><text x="160" y="242">relationships</text>
        <text x="313" y="214">Franchise</text><text x="313" y="228">sales</text><text x="313" y="242">expertise</text>
        <text x="465" y="214">Lead</text><text x="465" y="228">qualification</text><text x="465" y="242">systems</text>
        <text x="618" y="214">Franchise</text><text x="618" y="228">development</text><text x="618" y="242">processes</text>
        <text x="236" y="333">Industry</text><text x="236" y="347">connections</text>
        <text x="388" y="330">Candidate</text><text x="388" y="344">nurturing</text><text x="388" y="358">systems</text>
        <text x="541" y="328">CRM and</text><text x="541" y="342">reporting</text><text x="541" y="356">infrastructure</text>
      </g>
      <rect x="641" y="408" width="123" height="22" rx="4" fill="#13294b"/>
      <text x="702" y="422" text-anchor="middle" class="svg-head" font-size="7.2" font-weight="700" fill="#fff">OUTPOST LATTICE ADVISORS</text>
    </svg>
  </section>

  <!-- Slide 6: Broker community -->
  <section class="slide community" style="left:620px; top:753px;">
    <svg viewBox="0 0 775 436" aria-label="Instant access to the franchise broker community">
      <rect x="33" y="80" width="491" height="329" rx="14" fill="#13294b"/>
      <rect x="436" y="27" width="291" height="142" rx="10" fill="#f7971d"/>
      <g class="svg-head" font-size="19" font-weight="700" font-style="italic" fill="#13294b">
        <text x="470" y="65">We spent over 20 years</text>
        <text x="470" y="89">building these</text>
        <text x="470" y="113">relationships so your</text>
        <text x="470" y="137">brand doesn't have to.</text>
      </g>
      <g class="svg-head" font-size="26" font-weight="700">
        <text x="70" y="138" fill="#fff">Instant Access to</text>
        <text x="70" y="166" fill="#f7971d">the Franchise Broker</text>
        <text x="70" y="194" fill="#f7971d">Community</text>
      </g>
      <text x="70" y="244" class="svg-body" font-size="15.5" fill="#fff"><tspan fill="#f7971d">Outpost Lattice</tspan> Advisors in center Connecting to:</text>
      <g class="svg-body" font-size="15.5" fill="#fff">
        <text x="70" y="269">•</text><text x="85" y="269">Franchise consultants</text>
        <text x="70" y="295">•</text><text x="85" y="295">Broker networks</text>
        <text x="70" y="320">•</text><text x="85" y="320">Industry partners</text>
        <text x="70" y="345">•</text><text x="85" y="345">Referral sources</text>
        <text x="70" y="371">•</text><text x="85" y="371">Franchise influencers</text>
      </g>
      <g fill="#c9d1de">
        <rect x="542" y="198" width="90" height="34" rx="17"/>
        <rect x="650" y="194" width="76" height="44" rx="4"/>
        <rect x="540" y="258" width="94" height="22" rx="4"/>
        <rect x="664" y="254" width="56" height="26" rx="4"/>
        <rect x="542" y="306" width="88" height="34" rx="17"/>
      </g>
      <rect x="662" y="296" width="63" height="42" fill="#111"/>
      <line x1="436" y1="367" x2="727" y2="367" stroke="#f7971d" stroke-width="2"/>
      <rect x="641" y="408" width="123" height="22" rx="4" fill="#13294b"/>
      <text x="702" y="422" text-anchor="middle" class="svg-head" font-size="7.2" font-weight="700" fill="#fff">OUTPOST LATTICE ADVISORS</text>
    </svg>
  </section>

</main>
</body>
</html>
```